Flyer / Mailer for Business Debt Relief Business - Harborline Relief 6" x 11"

We need a 6" x 11" double sided flyer. This will be sent out to potential customers with high interest business loans. We would like the design to coordinate with the colors of our logo. I have included a mock up that we sketched out. I have also included a file of a mailer we received that we would like to use as a template (not colors or fonts, just set up). I have also included an .ai file of our logo.

```html
<!DOCTYPE html>
<html lang="en">
<head>
<meta charset="utf-8">
<title>Harborline Relief – Mailer</title>
<link href="https://fonts.googleapis.com/css2?family=Oswald:wght@600&family=Cabin:wght@400;500;700&display=swap" rel="stylesheet">
<style>
:root{
  --backdrop:#595959;
  --white:#ffffff;
  --blue:#0f6fc6;
  --blue-deep:#0b4f95;
  --title-blue:#1a6fc4;
  --green:#64a03a;
  --green-light:#7cc243;
  --charcoal:#3d3d3d;
  --pill:#3b3b3b;
  --ink:#333333;
}
*{box-sizing:border-box;margin:0;padding:0}
html,body{width:1200px;height:1200px;overflow:hidden;background:var(--backdrop);font-family:'Cabin',sans-serif}
.canvas{position:relative;width:1200px;height:1200px}

/* ---------- Front side ---------- */
.front{position:absolute;left:139px;top:122px;width:818px;height:446px;background:var(--white);overflow:hidden}
.photo-column{position:absolute;left:0;top:0;width:222px;height:446px;display:flex;flex-direction:column;gap:4px}
.photo{width:100%}
.photo--savings{height:148px;background:linear-gradient(135deg,#c97a5e,#e8d6c8 55%,#b9684f)}
.photo--couple{height:158px;background:linear-gradient(135deg,#d9c2a6,#c9a383 50%,#e3cdb4)}
.photo--growth{height:132px;background:radial-gradient(circle at 50% 30%,#9dc46a,#4c7a2b 55%,#3b2b1e)}

.front-main{position:absolute;left:222px;top:0;right:0;bottom:0}
.front-header{height:77px;display:flex;align-items:center;justify-content:space-between;padding:0 22px 0 10px}
.headline{font-family:'Oswald',sans-serif;font-weight:600;font-size:33px;color:var(--title-blue);letter-spacing:-.4px;transform:scaleX(.86);transform-origin:left center;white-space:nowrap}
.brand{display:flex;flex-direction:column;align-items:center;gap:5px}
.brand-mark{width:28px;height:28px;background:var(--green)}
.brand-name{font-size:9px;color:var(--ink);font-weight:500;letter-spacing:.4px}

.front-intro{height:63px;background:var(--green);padding:5px 14px;color:var(--white);font-weight:700;font-size:24px;line-height:25px;letter-spacing:-.3px}

.front-offer{position:relative;height:200px;background:var(--blue);overflow:hidden}
.offer-photo{position:absolute;right:0;top:0;width:330px;height:100%;background:linear-gradient(90deg,rgba(15,111,198,1) 0%,rgba(120,160,200,.6) 35%,#c8d4df 70%,#e6e2dc 100%)}
.offer-copy{position:relative;padding:6px 13px;color:var(--white)}
.offer-question{font-size:13px;font-weight:500}
.offer-callout{font-size:18px;font-weight:500;margin:2px 0 2px}
.benefits{list-style:none}
.benefits li{display:flex;align-items:center;gap:8px;font-size:10.3px;height:17px}
.benefits svg{width:11px;height:11px;flex:none}

.front-contact{position:absolute;left:0;right:0;top:342px;bottom:0;background:var(--green)}
.site-pill{position:absolute;left:73px;top:3px;width:454px;height:31px;border-radius:16px;background:var(--pill);color:var(--white);font-size:21px;text-align:center;line-height:31px;font-weight:500}
.contact-invite{position:absolute;right:315px;top:50px;text-align:right;color:var(--white);font-size:17.6px;line-height:22px;font-weight:500}
.contact-divider{position:absolute;left:307px;top:58px;width:2px;height:40px;background:var(--white)}
.contact-phone{position:absolute;left:325px;top:42px;display:flex;align-items:center;gap:6px;color:var(--white);font-size:31px;font-weight:700}
.contact-phone svg{width:20px;height:20px}
.contact-email{position:absolute;left:331px;top:84px;display:flex;align-items:center;gap:9px;color:var(--white);font-size:13px;font-weight:500}
.contact-email svg{width:15px;height:11px}

/* ---------- Back side ---------- */
.back{position:absolute;left:258px;top:625px;width:818px;height:446px;background:var(--white);overflow:hidden}
.back-panel{position:absolute;left:0;top:0;width:409px;height:446px}
.back-brand{height:122px;display:flex;flex-direction:column;align-items:center;justify-content:center;gap:12px;padding-top:6px}
.back-brand .brand-mark{width:52px;height:52px}
.back-brand .brand-name{font-size:17px;letter-spacing:1px;font-weight:400}
.back-address{height:48px;background:var(--charcoal);color:var(--white);text-align:center;font-size:14.5px;font-weight:500;line-height:18px;padding-top:6px}
.back-address svg{width:11px;height:14px;vertical-align:-1px;margin-right:7px}
.back-hero{position:relative;margin-top:3px;height:224px;background:var(--blue);overflow:hidden}
.hero-photo{position:absolute;right:0;top:0;width:210px;height:100%;background:radial-gradient(circle at 60% 55%,#3e86c9,#16406f 60%,#0b2c52)}
.hero-copy{position:relative;padding:17px 25px;color:var(--white)}
.hero-title{font-size:24px;font-weight:700;line-height:30px;letter-spacing:-.3px}
.hero-text{margin-top:7px;font-size:17px;line-height:21px;width:250px}
.hero-text strong{font-weight:700}
.back-site{height:33px;background:var(--green-light);color:var(--white);text-align:center;font-size:12.5px;font-weight:500;line-height:33px}
.back-site svg{width:10px;height:10px;vertical-align:-1px;margin-right:5px}
.back-foot{height:16px;background:var(--blue)}
</style>
</head>
<body>
<div class="canvas">

  <section class="front">
    <div class="photo-column">
      <div class="photo photo--savings" role="img" aria-label="Photo of a coin going into a white piggy bank"></div>
      <div class="photo photo--couple" role="img" aria-label="Photo of a couple saving money in a pink piggy bank"></div>
      <div class="photo photo--growth" role="img" aria-label="Photo of seedlings growing from rolled banknotes"></div>
    </div>

    <div class="front-main">
      <header class="front-header">
        <h1 class="headline">HELPING BUSINESSES FOCUS ON WHAT MATTERS!</h1>
        <div class="brand">
          <span class="brand-mark"></span>
          <span class="brand-name">Harborline Relief</span>
        </div>
      </header>

      <p class="front-intro">We understand that merchaat cash advance loans can be a burden on your business</p>

      <div class="front-offer">
        <div class="offer-photo" role="img" aria-label="Photo of business people shaking hands at a desk with a laptop"></div>
        <div class="offer-copy">
          <p class="offer-question">Overwhelmed by daly / weekly payments ?</p>
          <p class="offer-callout">WE CAN HELP !</p>
          <ul class="benefits">
            <li><svg viewBox="0 0 12 12"><rect x=".5" y=".5" width="11" height="11" fill="none" stroke="#fff"/><path d="M2.5 6l2.5 2.5 5-6" fill="none" stroke="#fff" stroke-width="1.6"/></svg>This is not a loan , we are not lenders</li>
            <li><svg viewBox="0 0 12 12"><rect x=".5" y=".5" width="11" height="11" fill="none" stroke="#fff"/><path d="M2.5 6l2.5 2.5 5-6" fill="none" stroke="#fff" stroke-width="1.6"/></svg>Imrove your business's cash flow immedictely</li>
            <li><svg viewBox="0 0 12 12"><rect x=".5" y=".5" width="11" height="11" fill="none" stroke="#fff"/><path d="M2.5 6l2.5 2.5 5-6" fill="none" stroke="#fff" stroke-width="1.6"/></svg>Move payments to one monthly amount</li>
            <li><svg viewBox="0 0 12 12"><rect x=".5" y=".5" width="11" height="11" fill="none" stroke="#fff"/><path d="M2.5 6l2.5 2.5 5-6" fill="none" stroke="#fff" stroke-width="1.6"/></svg>Reduce the amount you are pay us out monthly</li>
            <li><svg viewBox="0 0 12 12"><rect x=".5" y=".5" width="11" height="11" fill="none" stroke="#fff"/><path d="M2.5 6l2.5 2.5 5-6" fill="none" stroke="#fff" stroke-width="1.6"/></svg>Stretesic alternatives to high interest loans</li>
            <li><svg viewBox="0 0 12 12"><rect x=".5" y=".5" width="11" height="11" fill="none" stroke="#fff"/><path d="M2.5 6l2.5 2.5 5-6" fill="none" stroke="#fff" stroke-width="1.6"/></svg>Fast confidential business debt relief</li>
            <li><svg viewBox="0 0 12 12"><rect x=".5" y=".5" width="11" height="11" fill="none" stroke="#fff"/><path d="M2.5 6l2.5 2.5 5-6" fill="none" stroke="#fff" stroke-width="1.6"/></svg>No - obl sction consultation</li>
            <li><svg viewBox="0 0 12 12"><rect x=".5" y=".5" width="11" height="11" fill="none" stroke="#fff"/><path d="M2.5 6l2.5 2.5 5-6" fill="none" stroke="#fff" stroke-width="1.6"/></svg>Absolutely no credit polls</li>
            <li><svg viewBox="0 0 12 12"><rect x=".5" y=".5" width="11" height="11" fill="none" stroke="#fff"/><path d="M2.5 6l2.5 2.5 5-6" fill="none" stroke="#fff" stroke-width="1.6"/></svg>No collateral , no financials</li>
          </ul>
        </div>
      </div>

      <footer class="front-contact">
        <p class="site-pill">visit our website : www.harborlinerelief.com</p>
        <p class="contact-invite">Contact us now for FREE<br>consultation with our experts</p>
        <span class="contact-divider"></span>
        <p class="contact-phone"><svg viewBox="0 0 24 24"><path fill="#fff" d="M6.6 10.8a15.1 15.1 0 006.6 6.6l2.2-2.2a1 1 0 011-.25 11.4 11.4 0 003.6.6 1 1 0 011 1V20a1 1 0 01-1 1A17 17 0 013 4a1 1 0 011-1h3.5a1 1 0 011 1 11.4 11.4 0 00.6 3.6 1 1 0 01-.25 1z"/></svg>844-555-0187</p>
        <p class="contact-email"><svg viewBox="0 0 16 12"><rect x=".5" y=".5" width="15" height="11" fill="none" stroke="#fff"/><path d="M.5.5L8 7l7.5-6.5" fill="none" stroke="#fff"/></svg>info@harborlinerelief.com</p>
      </footer>
    </div>
  </section>

  <section class="back">
    <div class="back-panel">
      <div class="back-brand">
        <span class="brand-mark"></span>
        <span class="brand-name">Harborline Relief</span>
      </div>
      <p class="back-address"><svg viewBox="0 0 12 16"><path fill="#7cc243" d="M6 0a6 6 0 00-6 6c0 4.5 6 10 6 10s6-5.5 6-10a6 6 0 00-6-6zm0 8.5A2.5 2.5 0 116 3.5a2.5 2.5 0 010 5z"/></svg>1450 Cedar Ridge Dr<br>Brookfield, Dalton County 75012</p>
      <div class="back-hero">
        <div class="hero-photo" role="img" aria-label="Photo of cupped hands protecting a glowing dollar sign in front of a suit"></div>
        <div class="hero-copy">
          <h2 class="hero-title">Stratesic debt relief for<br>businesses of all sizes</h2>
          <p class="hero-text">stop takins out loans to pay off other loans.<br>Take back your business’s <strong>cash flow , and focus on what matters</strong></p>
        </div>
      </div>
      <p class="back-site"><svg viewBox="0 0 12 12"><circle cx="6" cy="6" r="5.3" fill="none" stroke="#fff"/><ellipse cx="6" cy="6" rx="2.3" ry="5.3" fill="none" stroke="#fff"/><path d="M.7 6h10.6" stroke="#fff"/></svg>www.harborlinerelief.com</p>
      <div class="back-foot"></div>
    </div>
  </section>

</div>
</body>
</html>
```